Recycling Exhibition Web Design Project

We are developing a new website for a exhibition we have just taken over. The previous site is very basic and we require a complete redesign. The site should be designed to engage with and attract those who work in or provide services to the multibillion dollar wastes and recycling industry in the Asia pacific region. These will include Federal & State Governments, City councils, private sector, industry associations and other key bodies, education facilities.

PLTX is the premier waste and recycling event in the Asia Pacific region and known as place where the industry meets to share innovations, gain knowledge, to network and do business.
• Innovation
• Knowledge transfer
• Industry Networking
• Trade
Key point: need to reflect that 2012 show will attract large numbers of quality visitors from across wide range of the industry – city councils, facilities managers, etc

Site should deliver 3 key objectives.
1. Stimulate interest those who work in or provide services to the wastes and recycling industry by providing simple to access, relevant and topical information about the Expo, the Seminars, the Key Features, the sub activities and the key benefits to them.
2. Provide a platform that supports / improves EP by providing a range of interactive components – ie floor plan / video. In addition options for sales enquiries, registration, general feedback
3. Provide a way to highlight / showcase sponsors, show features and other key assets. (possibly a carousel above the fold)

We really like the korba website so a take on this could be good (http://www.korba-example.com.au/). Also we want to try to reinforce the brand so we should use the event as the hero image/banner.

Previous website - http://www.pltx-example.com.au/

Target Market(s)

The site should be designed to engage with and attract those who work in or provide services to the multibillion dollar wastes and recycling industry

Industry/Entity Type

Recycling

Requirements
Must have
• The icons on the current site work quite well so inclusion as CTAs would be preferable.

Other key areas are

• Seminar Delegate & Visitor Registration
• Exhibitor Prospectus
• Floorplan
• Conference / Seminar content
• Social media + blog

Site visitors will need to feel like they are part of a community.
Site should reflect/display key industry stats & stats from 2011 expo

Please see the attached brief for more details and site map for menu items.

```html
<!DOCTYPE html>
<html lang="en">
<head>
<meta charset="utf-8">
<title>PLTX – Pacific Loop Trade Expo 2012</title>
<link href="https://fonts.googleapis.com/css2?family=Yanone+Kaffeesatz:wght@400;600&family=PT+Sans:wght@400;700&family=Arimo:wght@400;700&display=swap" rel="stylesheet">
<style>
:root{
  --wood:#8d877b;
  --wood-dark:#6f695e;
  --frame:#4b463f;
  --paper:#efece1;
  --card:#f7f6f1;
  --card-line:#dcd6b8;
  --green:#6d9852;
  --green-band:#3f6a2c;
  --red:#d24f4f;
  --gold:#c9b37e;
  --gold-text:#8a744d;
  --body:#4a4a46;
  --accent-green:#5e8a45;
  --footer:#c7bea7;
  --white:#ffffff;
}
*{box-sizing:border-box;margin:0;padding:0}
html,body{width:1200px;height:900px;overflow:hidden}
body{position:relative;background:linear-gradient(160deg,var(--wood) 0%,#9a9488 45%,var(--wood-dark) 100%);font-family:"Arimo",Arial,sans-serif;color:var(--body)}
.abs{position:absolute}

.account-tab{left:947px;top:0;width:184px;height:22px;background:#c9c1aa;border-radius:0 0 4px 4px;font:13px "Arimo",sans-serif;color:#3b3a36;display:flex;align-items:center;justify-content:center;gap:9px}
.account-tab .sep{color:#8c8470}

.brand{left:190px;top:24px;font:600 70px/1 "Yanone Kaffeesatz",sans-serif;color:#3a3631;letter-spacing:1px;white-space:nowrap}

.frame{left:91px;top:117px;width:1022px;height:700px;background:var(--frame);border-radius:3px;box-shadow:0 4px 14px rgba(0,0,0,.45)}
.paper{left:100px;top:126px;width:1004px;height:682px;background:var(--paper)}

.nav-ribbon{left:59px;top:137px;width:1119px;height:56px;background:linear-gradient(#7da562,var(--green));box-shadow:0 2px 5px rgba(0,0,0,.35)}
.nav-ribbon::before,.nav-ribbon::after{content:"";position:absolute;left:6px;right:6px;border-top:1px dashed rgba(255,255,255,.45)}
.nav-ribbon::before{top:5px}
.nav-ribbon::after{bottom:5px}
.ribbon-tail{top:150px;width:40px;height:58px}
.ribbon-tail.left{left:22px}
.ribbon-tail.right{left:1140px}
.main-nav a{position:absolute;top:154px;transform:translateX(-50%);font:700 17px "PT Sans",sans-serif;color:var(--white);text-decoration:none;text-transform:uppercase;text-shadow:0 1px 1px rgba(0,0,0,.35);white-space:nowrap}

.hero{left:108px;top:193px;width:984px;height:211px;background:linear-gradient(180deg,#c9cdc6 0%,#a7ae9c 45%,#6f8a4e 75%,#4d6a33 100%)}
.hero-copy{left:158px;top:248px;font:600 34px/1.14 "Yanone Kaffeesatz",sans-serif;color:var(--white);text-shadow:0 2px 3px rgba(0,0,0,.5)}

.sub-nav{left:108px;top:404px;width:984px;height:32px;background:var(--green-band)}
.sub-nav-link{position:absolute;top:413px;transform:translateX(-50%);font:13px "PT Sans",sans-serif;color:var(--white);text-decoration:none;text-transform:uppercase;white-space:nowrap}

.card{background:var(--card);border:1px solid var(--card-line);box-shadow:0 1px 2px rgba(0,0,0,.08)}
.intro-card{left:125px;top:453px;width:463px;height:104px}
.topics-card{left:125px;top:571px;width:463px;height:164px}
.event-card{left:607px;top:453px;width:474px;height:164px}
.sponsor-card{left:607px;top:633px;width:474px;height:102px}

.tag{display:flex;align-items:center;justify-content:center;font:600 22px "Yanone Kaffeesatz",sans-serif;color:var(--white);box-shadow:0 2px 3px rgba(0,0,0,.3)}
.tag-year{left:115px;top:472px;width:94px;height:58px;background:var(--red);font-size:34px;clip-path:polygon(0 0,88% 0,100% 50%,88% 100%,0 100%)}
.tag-topics{left:115px;top:584px;width:84px;height:30px;background:var(--green);clip-path:polygon(0 0,85% 0,100% 50%,85% 100%,0 100%)}
.tag-event{left:598px;top:466px;width:156px;height:30px;background:var(--green);clip-path:polygon(0 0,88% 0,100% 50%,88% 100%,0 100%)}
.tag-sponsors{left:600px;top:642px;width:84px;height:34px;background:var(--gold);clip-path:polygon(0 0,100% 0,92% 50%,100% 100%,0 100%)}

.intro-text{left:222px;top:470px;width:350px;font:14.5px/1.35 "Arimo",sans-serif;color:var(--body)}
.intro-text strong{font:600 21px "Yanone Kaffeesatz",sans-serif;color:var(--red)}

.topics-title{left:218px;top:584px;font:400 23px "Yanone Kaffeesatz",sans-serif;color:var(--accent-green)}
.more-info{left:508px;top:577px;font:13px "Arimo",sans-serif;color:var(--accent-green)}
.topics-list{left:159px;top:629px;list-style:none;font:14px/23px "Arimo",sans-serif;color:var(--body)}
.topics-list li::before{content:"";display:inline-block;width:6px;height:6px;background:var(--accent-green);margin-right:25px;vertical-align:middle}

.event-photo{left:622px;top:471px;width:444px;height:131px;background:linear-gradient(90deg,#8aa3b5 0%,#3a3f44 28%,#2d2c2a 45%,#7da48a 62%,#a8b2a8 80%,#5c7d98 100%)}

.sponsor-name{top:668px;height:46px;display:flex;align-items:center;font:700 22px "Arimo",sans-serif;white-space:nowrap}
.sponsor-korba{left:628px;color:#1b3c8f}
.sponsor-coastal{left:742px;color:#1c3d78;font-size:14px;line-height:1.2;width:170px;white-space:normal}
.sponsor-cirquetta{left:918px;color:#4aa238}
.dot{width:14px;height:14px;margin-right:8px;flex:none}
.dot.round{border-radius:50%;background:#4aa238}
.dot.square{background:#c9322e}
.carousel-next{left:1059px;top:668px;width:22px;height:32px;background:#e4e4e0;border-radius:3px}

.category-bar{left:98px;top:752px;width:1006px;height:52px;background:var(--gold)}
.category{position:absolute;top:762px;display:flex;align-items:center;gap:5px;font:11px/1.1 "Arimo",sans-serif;color:var(--gold-text);text-align:center}
.category svg{width:30px;height:30px;flex:none}

.footer{left:0;top:846px;width:1200px;height:54px;background:var(--footer);border-top:2px solid #a69d87}
.social{top:859px;width:36px;height:36px;border-radius:50%;background:#4a463f;border:2px solid #9c937d}
.footer-info{left:420px;top:869px;font:13px "Arimo",sans-serif;color:#4a463f}
.footer-info .sep{color:#8c8470;margin:0 8px}
.copyright{right:83px;top:869px;font:13px "Arimo",sans-serif;color:#4a463f}
</style>
</head>
<body>

<div class="abs account-tab"><span>Register</span><span class="sep">|</span><span>Exhibitor Login</span></div>
<div class="abs brand">Pacific Loop Trade Expo</div>

<div class="abs frame"></div>
<div class="abs paper"></div>

<svg class="abs ribbon-tail left" viewBox="0 0 40 58"><polygon points="0,0 40,0 40,58 0,58 14,29" fill="#567e3f"/></svg>
<svg class="abs ribbon-tail right" viewBox="0 0 40 58"><polygon points="0,0 40,0 26,29 40,58 0,58" fill="#567e3f"/></svg>
<div class="abs nav-ribbon"></div>
<nav class="main-nav">
  <a style="left:176px">Home</a>
  <a style="left:266px">About</a>
  <a style="left:398px">What's On</a>
  <a style="left:543px">Register</a>
  <a style="left:707px">How to Exhibit</a>
  <a style="left:865px">Blog</a>
  <a style="left:1008px">Contact Us</a>
</nav>

<div class="abs hero" role="img" aria-label="Photo of four coloured wheelie bins standing in a misty forest clearing"></div>
<div class="abs hero-copy">21 &amp; 22 November 2012<br>Harbourside Exhibition Hall<br>Cove Quay</div>

<div class="abs sub-nav"></div>
<nav class="sub-links">
  <a class="sub-nav-link" style="left:219px">Exhibition Prospectus</a>
  <a class="sub-nav-link" style="left:378px">Floor Plan</a>
  <a class="sub-nav-link" style="left:541px">Conferences / Seminars</a>
  <a class="sub-nav-link" style="left:710px">Registration</a>
  <a class="sub-nav-link" style="left:855px">Free Workshops</a>
  <a class="sub-nav-link" style="left:1004px">Our Sponsors</a>
</nav>

<section class="abs card intro-card"></section>
<div class="abs tag tag-year">2012</div>
<p class="abs intro-text"><strong>PLTX</strong> is the premier waste and recycling event in the Asia Pacific region. PLTX invites you to join &amp; share innovations, gain knowledge, &amp; to network.</p>

<section class="abs card topics-card"></section>
<div class="abs tag tag-topics">TOPICS</div>
<h2 class="abs topics-title">At the Conference</h2>
<a class="abs more-info">more info ★</a>
<ul class="abs topics-list">
  <li>Impact of the Carbon Price &amp; Carbon Farming Initiative</li>
  <li>Product Stewardship &amp; Innovation</li>
  <li>Waste to Energy &amp; Local Government AWT Procurement</li>
  <li>Green Buildings</li>
</ul>

<section class="abs card event-card"></section>
<div class="abs event-photo" role="img" aria-label="Photos of exhibition stands and sponsor banners at the 2011 expo"></div>
<div class="abs tag tag-event">★ 2011's EVENT</div>

<section class="abs card sponsor-card"></section>
<div class="abs sponsor-name sponsor-korba">korba</div>
<div class="abs sponsor-name sponsor-coastal"><span class="dot square"></span>Coastal Environment Office</div>
<div class="abs sponsor-name sponsor-cirquetta"><span class="dot round"></span>Cirquetta</div>
<div class="abs tag tag-sponsors">SPONSORS</div>
<svg class="abs carousel-next" viewBox="0 0 22 32"><polyline points="8,10 14,16 8,22" fill="none" stroke="#666" stroke-width="2.5"/></svg>

<div class="abs category-bar"></div>
<div class="category" style="left:112px"><svg viewBox="0 0 30 30"><polygon points="15,4 28,26 2,26" fill="none" stroke="#8a744d" stroke-width="2"/></svg>Hazardous<br>Waste</div>
<div class="category" style="left:216px"><svg viewBox="0 0 30 30"><rect x="7" y="7" width="16" height="16" fill="none" stroke="#8a744d" stroke-width="2" transform="rotate(30 15 15)"/></svg>Disposal</div>
<div class="category" style="left:320px"><svg viewBox="0 0 30 30"><circle cx="15" cy="15" r="10" fill="none" stroke="#8a744d" stroke-width="2"/></svg>Compost</div>
<div class="category" style="left:418px"><svg viewBox="0 0 30 30"><circle cx="15" cy="12" r="7" fill="none" stroke="#8a744d" stroke-width="2"/><rect x="12" y="20" width="6" height="6" fill="#8a744d"/></svg>Energy<br>from Waste</div>
<div class="category" style="left:524px"><svg viewBox="0 0 30 30"><rect x="8" y="6" width="14" height="20" fill="none" stroke="#8a744d" stroke-width="2"/></svg>Bin Liners<br>&amp; Containers</div>
<div class="category" style="left:640px"><svg viewBox="0 0 30 30"><circle cx="11" cy="15" r="6" fill="none" stroke="#8a744d" stroke-width="2"/><circle cx="21" cy="12" r="5" fill="none" stroke="#8a744d" stroke-width="2"/></svg>Machinery<br>&amp; Equipment</div>
<div class="category" style="left:768px"><svg viewBox="0 0 30 30"><rect x="4" y="7" width="22" height="17" fill="none" stroke="#8a744d" stroke-width="2"/><line x1="15" y1="7" x2="15" y2="24" stroke="#8a744d" stroke-width="2"/></svg>Service &amp;<br>Solutions</div>
<div class="category" style="left:886px"><svg viewBox="0 0 30 30"><rect x="3" y="9" width="16" height="12" fill="#8a744d"/><rect x="19" y="13" width="8" height="8" fill="#8a744d"/><circle cx="9" cy="23" r="3" fill="#c9b37e" stroke="#8a744d" stroke-width="2"/><circle cx="22" cy="23" r="3" fill="#c9b37e" stroke="#8a744d" stroke-width="2"/></svg>Vehicles<br>&amp; Plants</div>
<div class="category" style="left:1000px"><svg viewBox="0 0 30 30"><path d="M15 5 A10 10 0 1 1 5 15" fill="none" stroke="#8a744d" stroke-width="2.5"/><polygon points="15,1 20,5 15,9" fill="#8a744d"/></svg>Recycled<br>Products</div>

<footer class="abs footer"></footer>
<span class="abs social" style="left:87px" aria-label="Social link"></span>
<span class="abs social" style="left:136px" aria-label="Social link"></span>
<span class="abs social" style="left:188px" aria-label="Social link"></span>
<span class="abs social" style="left:239px" aria-label="Social link"></span>
<span class="abs social" style="left:288px" aria-label="Email link"></span>
<div class="abs footer-info">21 &amp; 22 November 2012<span class="sep">|</span>All Enquiries: +61 (3) 5550 0142</div>
<div class="abs copyright">© 2012 Pacific Loop Trade Expo</div>

</body>
</html>
```